Dermatology Office Business Card Update

Updating some information on the current business card. Do not adjust font type. Need both rounded rectangle and rounded square card files. In addition, must have separate file for both rectangle and square cards for gold foil printing.1. Update phone number with: 555-301-2846. Remove email address3. Add this website to be listed under clearhavenskinclinic.com:jilluxe.com4. Under updated phone number, add the photolake logo in color and then a space and the following text: @dermjill5. Gold foil should be inclusive of the outline of the butterfly wings on the front. Also should put a small hyphen that is also gold foil under the cursive Mona Perlow, MD and before the block lettering begins.Back of card remains the samePlease feel free to contact me with any questions!

Patients

Just needs some updates along with files for gold foil printing

• Updating some information on the current business card. Do not adjust font type. Need both rounded rectangle and rounded square card files. In addition, must have separate file for both rectangle and square cards for gold foil printing.
• 1. Update phone number with: 555-301-2846
• 2. Remove email address
• 3. Add this website to be listed under clearhavenskinclinic.com:
• monavea.com
• 4. Under updated phone number, add the photolake logo in color and then a space and the following text: @skinbymona
• 5. Gold foil should be inclusive of the outline of the butterfly wings on the front. Also should put a small hyphen that is also gold foil under the cursive Mona Perlow, MD and before the block lettering begins.
• Back of card remains the same
• Please feel free to contact me with any questions!

```html
<!DOCTYPE html>
<html lang="en">
<head>
<meta charset="utf-8">
<title>Clearhaven Skin Clinic — Business Cards</title>
<link rel="stylesheet" href="https://fonts.googleapis.com/css2?family=Montserrat:wght@500&family=Roboto:wght@400;500&display=swap">
<style>
  :root {
    --backdrop: #2c2c2e;
    --card: #ffffff;
    --navy: #2f3656;
    --mauve: #b08a8f;
    --gold: #b99a52;
    --ink: #3a3a3e;
    --wash-rose: #a9858b;
    --wash-plum: #8a7185;
    --wash-navy: #3d4a70;
  }
  * { box-sizing: border-box; margin: 0; padding: 0; }
  html, body { width: 1200px; height: 800px; overflow: hidden; }
  body { background: var(--backdrop); position: relative; font-family: "Roboto", Arial, sans-serif; }

  .card { position: absolute; width: 472px; height: 271px; overflow: hidden; }
  .card--rounded { border-radius: 20px; }
  .card--left { left: 92px; }
  .card--right { left: 647px; }
  .card--top { top: 117px; }
  .card--bottom { top: 461px; }

  .card-front { background: var(--card); }

  .brand { position: absolute; left: 0; right: 0; top: 26px; text-align: center; }
  .brand-dot { width: 40px; height: 40px; border-radius: 50%; background: var(--mauve); margin: 0 auto 14px; }
  .brand-name { font-family: "Montserrat", sans-serif; font-weight: 500; font-size: 12.5px; letter-spacing: 4.6px; line-height: 17px; color: var(--navy); text-transform: uppercase; padding-left: 4.6px; }

  .contact-block { position: absolute; top: 155px; left: 0; right: 0; display: flex; justify-content: center; }
  .card--right .contact-block { top: 161px; }
  .person { text-align: right; padding-right: 16px; }
  .person-name { font-size: 15.5px; font-weight: 500; color: var(--navy); line-height: 20px; }
  .person-title { font-size: 11px; color: var(--mauve); line-height: 18px; }
  .divider { width: 1px; background: var(--gold); height: 33px; margin-top: 2px; }
  .details { padding-left: 16px; padding-top: 3px; }
  .detail { display: flex; align-items: center; gap: 8px; font-size: 10px; color: var(--ink); line-height: 15px; }
  .detail svg { width: 9px; height: 9px; flex: none; }
  .social-mark { width: 8px; height: 8px; border-radius: 2px; background: #b5397d; flex: none; }

  .websites { position: absolute; left: 0; right: 0; top: 215px; text-align: center; font-size: 10px; color: var(--ink); display: flex; justify-content: center; align-items: center; gap: 7px; }
  .websites .sep { width: 1px; height: 7px; background: #999; }
  .websites .globe { width: 7px; height: 7px; border-radius: 50%; background: var(--gold); }
  .websites .pair { display: flex; align-items: center; gap: 5px; }
  .card--right .websites { top: 222px; gap: 12px; }

  .wash-band { position: absolute; left: 0; right: 0; bottom: 0; height: 22px;
    background: linear-gradient(90deg, var(--wash-navy) 0%, var(--wash-plum) 30%, var(--wash-rose) 60%, #b38d90 100%); }

  .card-back { background: radial-gradient(ellipse at 15% 30%, #b3959a 0%, transparent 55%),
    linear-gradient(160deg, var(--wash-rose) 0%, #947a88 45%, var(--wash-plum) 70%, var(--wash-navy) 100%); }
  .back-brand { position: absolute; left: 0; right: 0; top: 72px; text-align: center; }
  .back-brand .brand-dot { background: #ffffff; width: 48px; height: 48px; margin-bottom: 14px; }
  .back-brand .brand-name { color: #ffffff; }
  .tagline { position: absolute; left: 0; right: 0; top: 183px; text-align: center; font-family: "Montserrat", sans-serif; font-weight: 500; font-size: 12px; letter-spacing: 3.4px; color: #ffffff; padding-left: 3.4px; }
</style>
</head>
<body>

<section class="card card-front card--left card--top">
  <div class="brand">
    <div class="brand-dot"></div>
    <p class="brand-name">Clearhaven<br>Skin Clinic</p>
  </div>
  <div class="contact-block">
    <div class="person">
      <p class="person-name">Mona Perlow</p>
      <p class="person-title">MD</p>
    </div>
    <div class="divider"></div>
    <div class="details">
      <p class="detail"><svg viewBox="0 0 10 10"><path d="M2 1 L4 1 L4.6 3.2 L3.5 4 Q4.5 6 6 6.5 L7 5.4 L9 6 L9 8 Q8.5 9 7.5 9 Q2 8 1 2.5 Q1 1.5 2 1Z" fill="var(--gold)"/></svg>555-301-2846</p>
      <p class="detail"><span class="social-mark"></span>@skinbymona</p>
    </div>
  </div>
  <div class="websites">
    <span>www.clearhavenskinclinic.com</span><span class="sep"></span><span>www.monavea.com</span>
  </div>
  <div class="wash-band" role="img" aria-label="Watercolour wash band from navy to dusty rose"></div>
</section>

<section class="card card-front card--rounded card--right card--top">
  <div class="brand">
    <div class="brand-dot"></div>
    <p class="brand-name">Clearhaven<br>Skin Clinic</p>
  </div>
  <div class="contact-block">
    <div class="person">
      <p class="person-name">Mona Perlow</p>
      <p class="person-title">MD</p>
    </div>
    <div class="divider"></div>
    <div class="details">
      <p class="detail"><svg viewBox="0 0 10 10"><path d="M2 1 L4 1 L4.6 3.2 L3.5 4 Q4.5 6 6 6.5 L7 5.4 L9 6 L9 8 Q8.5 9 7.5 9 Q2 8 1 2.5 Q1 1.5 2 1Z" fill="var(--gold)"/></svg>555-301-2846</p>
      <p class="detail"><span class="social-mark"></span>@skinbymona</p>
    </div>
  </div>
  <div class="websites">
    <span class="pair"><span class="globe"></span>www.clearhavenskinclinic.com</span>
    <span class="pair"><span class="globe"></span>www.monavea.com</span>
  </div>
  <div class="wash-band" role="img" aria-label="Watercolour wash band from navy to dusty rose"></div>
</section>

<section class="card card-back card--left card--bottom" role="img" aria-label="Dusty rose to navy watercolour background">
  <div class="back-brand">
    <div class="brand-dot"></div>
    <p class="brand-name">Clearhaven<br>Skin Clinic</p>
  </div>
  <p class="tagline">RADIANTLY YOU</p>
</section>

<section class="card card-back card--rounded card--right card--bottom" role="img" aria-label="Dusty rose to navy watercolour background">
  <div class="back-brand">
    <div class="brand-dot"></div>
    <p class="brand-name">Clearhaven<br>Skin Clinic</p>
  </div>
  <p class="tagline">RADIANTLY YOU</p>
</section>

</body>
</html>
```